Business Card Design Project

New Business Card design for Varodine Technology Ltd using new Logo and new Tagline for staffing company.

About us from our website - www.varodine.example:

VaroDine is a leading and recognized Electronic Entertainment, Workforce Augmentation, and Project Management solutions provider with clients in Electronic Entertainment, Legal, Technology, Government and other verticals that range in size from start up organizations to Zenlar 500 companies. VaroDine is certified as an 8(a) minority and woman owned enterprise, established in 1998.

Target Market(s)

Companies in Electronic Entertainment, Legal, Government and Technology

Industry/Entity Type

Business

Requirements
Must have
• Must include in small letters the following information on back:

Established in 1998
8(a)(w)(e), Cage #7KRT9, DUNS #462137580

Front should have the following:
Derek Holloway
Vice President
5820 Birchmont Road
Fallowby, FB 482917
555-318-2746 X 100
555-902-6613 Fax
555-318-2746 Toll Free
name@varodine.example

Our Tagline: Connect • Collaborate • Achieve

```html
<!DOCTYPE html>
<html lang="en">
<head>
<meta charset="utf-8">
<title>VaroDine Business Card</title>
<link href="https://fonts.googleapis.com/css2?family=Arimo:wght@400;700&family=Pinyon+Script&display=swap" rel="stylesheet">
<style>
  :root {
    --page: #ffffff;
    --teal-light: #11998a;
    --teal: #0b6f69;
    --teal-dark: #052624;
    --blue-deep: #1f4a5e;
    --blue-bright: #2aa3dc;
    --brand-blue: #1e63b5;
    --white: #ffffff;
    --frame: rgba(200, 220, 220, 0.45);
    --text-shadow: rgba(0, 0, 0, 0.85);
  }
  * { margin: 0; padding: 0; box-sizing: border-box; }
  html, body {
    width: 879px; height: 1200px; overflow: hidden;
    background: var(--page);
  }
  .canvas { position: relative; width: 879px; height: 1200px; }
  .card {
    position: absolute; left: 28px; width: 819px; overflow: hidden;
    font-family: "Arimo", Arial, sans-serif; font-weight: 700; color: var(--white);
  }
  .card-front { top: 35px; height: 538px; }
  .card-back { top: 624px; height: 547px; box-shadow: 4px 6px 8px rgba(0,0,0,0.25); }
  .card-bg { position: absolute; inset: 0; width: 100%; height: 100%; }
  .inner-frame {
    position: absolute; inset: 18px; border: 1px solid var(--frame);
  }
  .brand-name {
    position: absolute; font-family: "Arimo", Arial, sans-serif; font-weight: 700;
    color: var(--white); letter-spacing: -0.5px; line-height: 1;
  }
  .brand-mark {
    position: absolute; border-radius: 50%; background: var(--brand-blue);
  }
  .card-front .brand-name { left: 32px; top: 68px; font-size: 46px; }
  .card-front .brand-mark { left: 262px; top: 76px; width: 28px; height: 28px; }
  .person-name {
    position: absolute; right: 42px; top: 44px;
    font-family: "Pinyon Script", cursive; font-weight: 400; font-size: 48px; line-height: 1;
  }
  .person-title {
    position: absolute; right: 44px; top: 104px; font-size: 20px; line-height: 24px;
  }
  .contact-list {
    position: absolute; right: 44px; top: 312px; list-style: none; text-align: right;
    font-size: 20px; line-height: 31px;
    text-shadow: 1px 1px 2px var(--text-shadow), 0 0 3px var(--text-shadow);
  }
  .card-back .brand-name { left: 62px; top: 115px; font-size: 98px; }
  .card-back .brand-mark { left: 490px; top: 150px; width: 44px; height: 44px; }
  .sector-icon {
    position: absolute; border-radius: 50%;
    border: 4px solid #e9f2f6; box-shadow: 0 2px 6px rgba(0,0,0,0.4);
  }
  .sector-government { left: 487px; top: 323px; width: 96px; height: 96px;
    background: radial-gradient(circle at 40% 40%, #3f8fb0, #1c4d66); }
  .sector-entertainment { left: 594px; top: 285px; width: 86px; height: 86px;
    background: radial-gradient(circle at 40% 40%, #4fa4c6, #215a76); }
  .sector-legal { left: 691px; top: 324px; width: 86px; height: 86px;
    background: radial-gradient(circle at 40% 40%, #4aa6d0, #1f5877); }
  .back-text {
    position: absolute; left: 0; width: 938px; top: 438px; text-align: center;
    text-shadow: 2px 2px 2px var(--text-shadow);
  }
  .tagline { font-size: 26px; line-height: 34px; }
  .credentials { font-size: 14px; font-weight: 400; line-height: 18px; margin-top: 2px; }
</style>
</head>
<body>
<main class="canvas">

  <section class="card card-front">
    <svg class="card-bg" viewBox="0 0 819 538" preserveAspectRatio="none" aria-hidden="true">
      <defs>
        <radialGradient id="frontBg" cx="0.1" cy="0.05" r="1.1">
          <stop offset="0" stop-color="#11998a"/>
          <stop offset="0.45" stop-color="#0b6f69"/>
          <stop offset="1" stop-color="#052624"/>
        </radialGradient>
        <radialGradient id="lightSwirl" cx="0.55" cy="0.55" r="0.5">
          <stop offset="0" stop-color="#ffffff" stop-opacity="0.95"/>
          <stop offset="0.35" stop-color="#cfeff4" stop-opacity="0.55"/>
          <stop offset="1" stop-color="#9fdde6" stop-opacity="0"/>
        </radialGradient>
      </defs>
      <rect width="819" height="538" fill="url(#frontBg)"/>
      <g role="img" aria-label="Flowing ribbons of white-blue light sweeping across the card">
        <ellipse cx="430" cy="270" rx="390" ry="210" fill="url(#lightSwirl)" transform="rotate(-12 430 270)"/>
      </g>
    </svg>
    <div class="inner-frame"></div>
    <div class="brand-name">VaroDine</div>
    <div class="brand-mark"></div>
    <div class="person-name">Derek Holloway</div>
    <div class="person-title">Vice President</div>
    <ul class="contact-list">
      <li>5820 Birchmont Road</li>
      <li>Fallowby, FB 482917</li>
      <li>555-318-2746 X 100</li>
      <li>555-902-6613 Fax</li>
      <li>555-318-2746 Toll Free</li>
      <li>name@varodine.example</li>
    </ul>
  </section>

  <section class="card card-back">
    <svg class="card-bg" viewBox="0 0 819 547" preserveAspectRatio="none" aria-hidden="true">
      <defs>
        <radialGradient id="backBg" cx="0.05" cy="0" r="1">
          <stop offset="0" stop-color="#11998a"/>
          <stop offset="0.5" stop-color="#0a5e5a"/>
          <stop offset="1" stop-color="#052624"/>
        </radialGradient>
        <linearGradient id="wave" x1="0.2" y1="0.2" x2="1" y2="1">
          <stop offset="0" stop-color="#1f3f4c"/>
          <stop offset="0.55" stop-color="#2a6a86"/>
          <stop offset="1" stop-color="#2aa3dc"/>
        </linearGradient>
      </defs>
      <rect width="819" height="547" fill="url(#backBg)"/>
      <path d="M819 0 C700 70 540 150 400 260 C260 370 130 470 0 547 L819 547 Z" fill="url(#wave)"/>
      <path d="M819 0 C700 70 540 150 400 260 C260 370 130 470 0 547" fill="none" stroke="#9fd3dc" stroke-opacity="0.35" stroke-width="2"/>
    </svg>
    <div class="inner-frame"></div>
    <div class="brand-name">VaroDine</div>
    <div class="brand-mark"></div>
    <div class="sector-icon sector-government" role="img" aria-label="Government badge icon"></div>
    <div class="sector-icon sector-entertainment" role="img" aria-label="Game controller icon"></div>
    <div class="sector-icon sector-legal" role="img" aria-label="Judge's gavel icon"></div>
    <div class="back-text">
      <p class="tagline">Connect • Collaborate • Achieve</p>
      <p class="credentials">Established in 1998<br>8(a)(w)(e), Cage #7KRT9, DUNS #462137580</p>
    </div>
  </section>

</main>
</body>
</html>
```